App Redesign for PathMentor

We're looking for a skilled UI/UX designer to modernize the PathMentor mobile app, enhancing user engagement while preserving our current brand identity.

Key Objectives:
Refresh the app using modern design trends
Maintain a clean, calm, and playful aesthetic aligned with our brand
Boost engagement through improved flow, visuals, and interactivity

Design Requirements:
Retain recognizability from our app and website (see Brand ID Guide) (and website pathmentorhub.example)
Reflect a tone that is supportive, fun/ playful, and professional

Design 5–8 key screens, including:
Home/Dashboard
Daily Intentions Interface
Gamification Overview (Streaks, Rewards)
Social Features (Direct Realtime Feedback, Messaging, Challenges)
Progress Tracking

New Feature Concepts to Include:
Daily Intentions with voice/text input and visual encouragement
Gamification elements like streaks, badges, and animations
Social Connections including messaging, reactions, and feedback tools
Optional: Subtle design cues for future AI-driven interactions

Audience: Adults aged 25–55 interested in personal development and coaching. Tech-comfortable but not tech-savvy.

Visual Inspiration: Wordivo (gamification), Calmnest (intentions), Runqo (social support)

Target Market(s)

Corporate Leaders and Entrepreneurs

Industry/Entity Type

Leadership Training & Consultancies

Font styles to use
Sans Serif
Other font styles liked:
• Avenir, Arial

Colors
FFF300
FFF600
FEFA6F
FFFEC7
FFFEE8

Requirements
Nice to have
• Wordivo, Calmnest,

```html
<!DOCTYPE html>
<html lang="en">
<head>
<meta charset="utf-8">
<title>PathMentor – App Screens</title>
<link href="https://fonts.googleapis.com/css2?family=Figtree:wght@400;500;600;700&display=swap" rel="stylesheet">
<style>
:root{
  --bg:#E4E4E4;
  --yellow:#FFD600;
  --yellow-deep:#EDC200;
  --yellow-soft:#F8E79A;
  --yellow-chip:#FCEDA0;
  --grey-nav:#B4ADA7;
  --grey-card:#BBB5B0;
  --grey-bubble:#EEE6E3;
  --ink:#1E1E1E;
  --muted:#A9A9A9;
  --line:#E6E6E6;
  --orange:#F7A400;
  --green:#2ECC71;
  --white:#FFFFFF;
}
*{box-sizing:border-box;margin:0;padding:0}
html,body{width:1200px;height:1088px;overflow:hidden}
body{background:var(--bg);font-family:'Figtree',Arial,sans-serif;color:var(--ink);position:relative}
.phone{position:absolute;top:47px;width:311px;background:var(--white);border-radius:30px;overflow:hidden;box-shadow:0 6px 18px rgba(0,0,0,.08)}
.phone--home{left:67px;height:989px}
.phone--intentions{left:441px;height:600px}
.phone--social{left:815px;height:600px}
.header{position:absolute;top:0;left:0;right:0;height:98px;background:var(--yellow);border-radius:0 0 70px 70px/0 0 46px 46px;overflow:hidden}
.header__blob{position:absolute;left:155px;top:-30px;width:200px;height:150px;border-radius:50%;background:var(--yellow-deep)}
.header__pill{position:absolute;left:180px;top:22px;width:106px;height:40px;border-radius:20px;background:var(--yellow)}
.status{position:absolute;top:11px;left:16px;right:16px;display:flex;justify-content:space-between;align-items:center;font-size:10.5px;font-weight:600;z-index:2}
.status__icons{display:flex;gap:6px;align-items:center}
.title{position:absolute;top:33px;left:0;right:0;text-align:center;font-size:18px;font-weight:700;z-index:2}
.home-glyph{position:absolute;top:35px;left:147px;width:17px;height:17px;z-index:2}
.brand{position:absolute;left:35px;top:65px;width:242px;height:55px;border-radius:28px;background:var(--white);box-shadow:0 5px 10px rgba(0,0,0,.12);display:flex;align-items:center;justify-content:center;gap:10px;z-index:3}
.brand__dot{width:24px;height:24px;border-radius:50%;background:var(--yellow)}
.brand__name{font-size:19px;font-weight:700;color:#F2C000}
.label{position:absolute;left:15px;font-size:16px;font-weight:400}
.stat{position:absolute;top:172px;width:131px;height:52px;border-radius:4px;padding:7px 12px}
.stat--grey{left:15px;background:var(--grey-card)}
.stat--yellow{left:161px;background:var(--yellow)}
.stat__num{font-size:17px;font-weight:700;line-height:1.1}
.stat__text{font-size:11.5px}
.stat svg{position:absolute;right:9px;top:8px}
.card{position:absolute;background:var(--white);box-shadow:0 2px 8px rgba(0,0,0,.08)}
.card__title{position:absolute;left:11px;top:14px;right:8px;font-size:10px;font-weight:700;line-height:1.4;color:#333}
.card svg{position:absolute;left:0;top:0}
.field{position:absolute;left:15px;width:280px;height:42px;border:1px solid var(--line);border-radius:21px;padding:0 21px;display:flex;align-items:center;justify-content:space-between;font-size:13px;color:#C9C9C9}
.chip{position:absolute;top:365px;height:42px;border-radius:21px;background:var(--yellow-chip);display:flex;align-items:center;justify-content:center;gap:8px;font-size:14px;font-weight:500}
.timer{position:absolute;left:15px;top:461px;font-size:17px}
.timer small{font-size:11px}
.timer__sub{position:absolute;left:15px;top:488px;font-size:10px;color:#C4C4C4}
.toggle{position:absolute;left:236px;top:467px;width:59px;height:32px;border-radius:16px;background:var(--grey-card)}
.toggle::after{content:"";position:absolute;right:4px;top:4px;width:24px;height:24px;border-radius:50%;background:var(--white)}
.bubble{position:absolute;height:36px;width:179px;border-radius:18px;display:flex;align-items:center;padding-left:22px;font-size:12.5px}
.bubble--in{left:16px;background:var(--grey-bubble)}
.bubble--out{left:116px;background:var(--yellow-soft);justify-content:center;padding-left:0}
.composer{position:absolute;left:16px;top:480px;width:235px;height:35px;border-radius:18px;background:var(--white);box-shadow:0 2px 8px rgba(0,0,0,.08);display:flex;align-items:center;gap:8px;padding:0 9px;font-size:10.5px;color:#CFCFCF}
.composer__tools{margin-left:auto;display:flex;gap:12px;align-items:center}
.mic-btn{position:absolute;left:258px;top:479px;width:36px;height:36px;border-radius:50%;background:var(--yellow);display:flex;align-items:center;justify-content:center}
.nav{position:absolute;left:0;right:0;bottom:0;height:65px;background:var(--grey-nav)}
.nav__item{position:absolute;top:18px;transform:translateX(-50%);display:flex;flex-direction:column;align-items:center;color:var(--white);font-size:6.5px;line-height:1.25;text-align:center;white-space:nowrap}
.nav__item svg{width:19px;height:19px;margin-bottom:3px}
.nav__active{position:absolute;top:-16px;width:48px;height:48px;transform:translateX(-50%);border-radius:50%;background:var(--yellow);box-shadow:0 0 0 6px var(--white);display:flex;align-items:center;justify-content:center;color:var(--white)}
.nav__active svg{width:24px;height:24px}
.nav__active-label{position:absolute;bottom:5px;transform:translateX(-50%);color:var(--white);font-size:9px;white-space:nowrap}
.axis text{font-family:'Figtree',Arial,sans-serif}
</style>
</head>
<body>
<svg width="0" height="0" style="position:absolute">
  <defs>
    <symbol id="i-home" viewBox="0 0 24 24"><path fill="currentColor" d="M12 3 1.5 12.5H5V21h5v-5h4v5h5v-8.5h3.5z"/></symbol>
    <symbol id="i-social" viewBox="0 0 24 24"><g fill="currentColor"><circle cx="6.5" cy="6.5" r="4.5"/><rect x="13" y="2" width="9" height="9" rx="2"/><path d="M6.5 13 2 21.5h9z"/><path d="M17.5 22 13.3 17.6a2.6 2.6 0 0 1 4.2-3 2.6 2.6 0 0 1 4.2 3z"/></g></symbol>
    <symbol id="i-target" viewBox="0 0 24 24"><g fill="none" stroke="currentColor" stroke-width="2.2"><circle cx="11" cy="13" r="9"/><circle cx="11" cy="13" r="4.6"/><path d="M11 13 21 3M17 3h4v4"/></g><circle cx="11" cy="13" r="1.6" fill="currentColor"/></symbol>
    <symbol id="i-game" viewBox="0 0 24 24"><path fill="currentColor" d="M7 7h10a5 5 0 0 1 5 5l1 6a2.5 2.5 0 0 1-4.4 1.8L16 17H8l-2.6 2.8A2.5 2.5 0 0 1 1 18l1-6a5 5 0 0 1 5-5zm0 3v2H5v2h2v2h2v-2h2v-2H9v-2zm9 1a1 1 0 1 0 0 2 1 1 0 0 0 0-2zm2 2a1 1 0 1 0 0 2 1 1 0 0 0 0-2zM11 3h2v4h-2z"/></symbol>
    <symbol id="i-progress" viewBox="0 0 24 24"><path fill="currentColor" d="M8 2h8v3H8zM5 4h2v3h10V4h2v15H5zm3 6v2h8v-2zm0 4v2h6v-2zM9 20h6v2H9z"/></symbol>
    <symbol id="i-mic" viewBox="0 0 24 24"><path fill="currentColor" d="M12 2a3.5 3.5 0 0 1 3.5 3.5v6a3.5 3.5 0 0 1-7 0v-6A3.5 3.5 0 0 1 12 2zm-7 9h2a5 5 0 0 0 10 0h2a7 7 0 0 1-6 6.9V21h3v2H8v-2h3v-3.1A7 7 0 0 1 5 11z"/></symbol>
    <symbol id="i-status" viewBox="0 0 60 12"><g fill="currentColor"><rect x="0" y="8" width="2" height="3"/><rect x="3" y="6" width="2" height="5"/><rect x="6" y="4" width="2" height="7"/><rect x="9" y="1" width="2" height="10"/><path d="M29 11l-2.2-2.4a3 3 0 0 1 4.4 0zM24.6 6.3a6.3 6.3 0 0 1 8.8 0l-1.3 1.4a4.4 4.4 0 0 0-6.2 0zM22.4 4a9.5 9.5 0 0 1 13.2 0l-1.3 1.4a7.6 7.6 0 0 0-10.6 0z"/><rect x="44" y="2" width="14" height="8" rx="1.5" fill="none" stroke="currentColor" stroke-width="1.2"/><rect x="45.5" y="3.5" width="11" height="5" rx=".5"/><rect x="58.5" y="4.5" width="1.3" height="3"/></g></symbol>
  </defs>
</svg>

<!-- Home / Dashboard -->
<section class="phone phone--home">
  <div class="header"><div class="header__blob"></div><div class="header__pill"></div></div>
  <div class="status"><span>8:41 Am</span><svg width="58" height="12"><use href="#i-status"/></svg></div>
  <svg class="home-glyph" viewBox="0 0 24 24"><use href="#i-home"/></svg>
  <div class="brand"><span class="brand__dot"></span><span class="brand__name">PathMentor</span></div>

  <div class="label" style="top:188px">PeakMind<sup style="font-size:6px">TM</sup> Tracker</div>
  <div class="stat stat--grey">
    <div class="stat__num">271</div><div class="stat__text">Weekly Reports</div>
    <svg width="22" height="22" viewBox="0 0 24 24"><use href="#i-progress"/></svg>
  </div>
  <div class="stat stat--yellow">
    <div class="stat__num">75</div><div class="stat__text">Monthly Reports</div>
    <svg width="22" height="22" viewBox="0 0 24 24"><use href="#i-progress"/></svg>
  </div>

  <div class="label" style="top:290px">Your Overall Progress</div>
  <div class="card" style="left:15px;top:275px;width:279px;height:155px">
    <svg width="279" height="155" viewBox="0 0 372 207" class="axis">
      <g stroke="#E5E5E5" stroke-width="1">
        <line x1="48" y1="24" x2="358" y2="24"/><line x1="48" y1="54" x2="358" y2="54"/><line x1="48" y1="84" x2="358" y2="84"/>
        <line x1="48" y1="114" x2="358" y2="114"/><line x1="48" y1="144" x2="358" y2="144"/><line x1="48" y1="174" x2="358" y2="174"/>
      </g>
      <g fill="#A8A8A8" font-size="13" text-anchor="middle">
        <text x="28" y="29">100</text><text x="28" y="59">80</text><text x="28" y="89">60</text>
        <text x="28" y="119">40</text><text x="28" y="149">20</text><text x="28" y="179">10</text>
      </g>
      <polyline fill="none" stroke="#555" stroke-width="1.2" points="57,105 82,94 107,111 132,118 156,124 181,127 206,113 231,123 256,120 281,119 305,124 330,121"/>
      <g fill="#fff" stroke="#F2C400" stroke-width="1.8">
        <circle cx="57" cy="105" r="3"/><circle cx="82" cy="94" r="3"/><circle cx="107" cy="111" r="3"/><circle cx="132" cy="118" r="3"/>
        <circle cx="156" cy="124" r="3"/><circle cx="181" cy="127" r="3"/><circle cx="206" cy="113" r="3"/><circle cx="231" cy="123" r="3"/>
        <circle cx="256" cy="120" r="3"/><circle cx="281" cy="119" r="3"/><circle cx="305" cy="124" r="3"/><circle cx="330" cy="121" r="3"/>
      </g>
    </svg>
  </div>

  <div class="label" style="top:490px">Your Growth</div>
  <div class="card" style="left:16px;top:474px;width:278px;height:191px">
    <svg width="278" height="191" viewBox="0 0 371 255" class="axis">
      <g fill="#C8C8C8" font-size="10" text-anchor="middle">
        <text x="28" y="81">5.0</text><text x="28" y="94">4.5</text><text x="28" y="107">4.0</text><text x="28" y="119">3.5</text>
        <text x="28" y="132">3.0</text><text x="28" y="145">2.5</text><text x="28" y="157">2.0</text><text x="28" y="170">1.5</text>
        <text x="28" y="183">1.0</text><text x="28" y="195">0.5</text><text x="28" y="208">0</text>
      </g>
      <line x1="65" y1="78" x2="355" y2="78" stroke="#F6C6A6" stroke-width="1.5"/>
      <g fill="var(--orange)">
        <rect x="74" y="180" width="9" height="25"/><rect x="99" y="180" width="9" height="25"/><rect x="112" y="154" width="9" height="51"/>
        <rect x="124" y="180" width="9" height="25"/><rect x="137" y="154" width="9" height="51"/><rect x="150" y="154" width="9" height="51"/>
        <rect x="162" y="154" width="9" height="51"/><rect x="200" y="103" width="9" height="102"/><rect x="212" y="154" width="9" height="51"/>
        <rect x="225" y="180" width="9" height="25"/><rect x="237" y="180" width="9" height="25"/><rect x="250" y="154" width="9" height="51"/>
        <rect x="262" y="154" width="9" height="51"/><rect x="275" y="154" width="9" height="51"/><rect x="287" y="180" width="9" height="25"/>
        <rect x="300" y="154" width="9" height="51"/><rect x="313" y="180" width="9" height="25"/><rect x="325" y="129" width="9" height="76"/>
        <rect x="350" y="180" width="9" height="25"/>
      </g>
      <g fill="#D4D4D4" font-size="9" text-anchor="end">
        <text transform="translate(68 222) rotate(-50)">Wk 50</text><text transform="translate(93 222) rotate(-50)">Wk 1</text>
        <text transform="translate(118 222) rotate(-50)">Wk 3</text><text transform="translate(143 222) rotate(-50)">Wk 5</text>
        <text transform="translate(168 222) rotate(-50)">Wk 7</text><text transform="translate(193 222) rotate(-50)">Wk 9</text>
        <text transform="translate(218 222) rotate(-50)">Wk 11</text><text transform="translate(243 222) rotate(-50)">Wk 13</text>
        <text transform="translate(268 222) rotate(-50)">Wk 15</text><text transform="translate(293 222) rotate(-50)">Wk 17</text>
        <text transform="translate(318 222) rotate(-50)">Wk 19</text><text transform="translate(343 222) rotate(-50)">Wk 21</text>
      </g>
    </svg>
    <div class="card__title">BODY: Did I take a cold shower or swim in the river today?</div>
  </div>

  <div class="card" style="left:16px;top:686px;width:279px;height:191px">
    <svg width="279" height="191" viewBox="0 0 373 255" class="axis">
      <g fill="#C8C8C8" font-size="10" text-anchor="middle">
        <text x="28" y="71">7</text><text x="28" y="89">6</text><text x="28" y="107">5</text><text x="28" y="124">4</text>
        <text x="28" y="142">3</text><text x="28" y="160">2</text><text x="28" y="177">1</text><text x="28" y="195">0</text>
      </g>
      <g>
        <rect x="56" y="86" width="9" height="106" fill="var(--green)"/><rect x="69" y="86" width="9" height="106" fill="var(--green)"/>
        <rect x="82" y="118" width="9" height="74" fill="var(--orange)"/><rect x="95" y="86" width="9" height="106" fill="var(--green)"/>
        <rect x="108" y="89" width="9" height="103" fill="var(--orange)"/><rect x="121" y="86" width="9" height="106" fill="var(--green)"/>
        <rect x="134" y="95" width="9" height="97" fill="var(--orange)"/><rect x="147" y="86" width="9" height="106" fill="var(--green)"/>
        <rect x="160" y="68" width="9" height="124" fill="var(--green)"/><rect x="173" y="89" width="9" height="103" fill="var(--orange)"/>
        <rect x="186" y="91" width="9" height="101" fill="var(--orange)"/><rect x="199" y="86" width="9" height="106" fill="var(--green)"/>
        <rect x="212" y="86" width="9" height="106" fill="var(--green)"/><rect x="225" y="86" width="9" height="106" fill="var(--green)"/>
        <rect x="238" y="82" width="9" height="110" fill="var(--green)"/><rect x="251" y="91" width="9" height="101" fill="var(--orange)"/>
        <rect x="264" y="80" width="9" height="112" fill="var(--green)"/><rect x="277" y="89" width="9" height="103" fill="var(--orange)"/>
        <rect x="290" y="86" width="9" height="106" fill="var(--green)"/><rect x="303" y="96" width="9" height="96" fill="var(--orange)"/>
        <rect x="316" y="68" width="9" height="124" fill="var(--green)"/><rect x="329" y="121" width="9" height="71" fill="var(--orange)"/>
      </g>
      <line x1="56" y1="85" x2="346" y2="85" stroke="#F6B58E" stroke-width="1.3"/>
      <line x1="56" y1="139" x2="346" y2="139" stroke="#333" stroke-width="1"/>
      <g fill="#D4D4D4" font-size="9" text-anchor="end">
        <text transform="translate(60 212) rotate(-50)">Wk 50</text><text transform="translate(86 212) rotate(-50)">Wk 1</text>
        <text transform="translate(112 212) rotate(-50)">Wk 3</text><text transform="translate(138 212) rotate(-50)">Wk 5</text>
        <text transform="translate(164 212) rotate(-50)">Wk 7</text><text transform="translate(190 212) rotate(-50)">Wk 10</text>
        <text transform="translate(216 212) rotate(-50)">Wk 12</text><text transform="translate(242 212) rotate(-50)">Wk 14</text>
        <text transform="translate(268 212) rotate(-50)">Wk 16</text><text transform="translate(294 212) rotate(-50)">Wk 18</text>
        <text transform="translate(320 212) rotate(-50)">Wk 20</text><text transform="translate(346 212) rotate(-50)">Wk 22</text>
      </g>
    </svg>
    <div class="card__title" style="left:15px;top:22px">BALANCE: what was focus in family activities?</div>
  </div>

  <nav class="nav">
    <div class="nav__active" style="left:70px"><svg><use href="#i-home"/></svg></div>
    <span class="nav__active-label" style="left:69px">Home</span>
    <div class="nav__item" style="left:125px"><svg><use href="#i-social"/></svg>Social<br>Features</div>
    <div class="nav__item" style="left:172px"><svg><use href="#i-target"/></svg>Daily<br>Intensions</div>
    <div class="nav__item" style="left:224px"><svg><use href="#i-game"/></svg>Gamification</div>
    <div class="nav__item" style="left:276px"><svg><use href="#i-progress"/></svg>Progress<br>Tracking</div>
  </nav>
</section>

<!-- Daily Intentions -->
<section class="phone phone--intentions">
  <div class="header"><div class="header__blob"></div><div class="header__pill"></div></div>
  <div class="status"><span>8:41 Am</span><svg width="58" height="12"><use href="#i-status"/></svg></div>
  <div class="title">Daily Intentions</div>
  <div class="brand"><span class="brand__dot"></span><span class="brand__name">PathMentor</span></div>

  <div class="label" style="top:150px">What will help you grow today?</div>
  <div class="field" style="top:181px">Type Here</div>
  <div class="label" style="top:240px">Enter intentions?</div>
  <div class="field" style="top:271px">Type Here<svg width="16" height="20" viewBox="0 0 24 24" style="color:#CFCFCF"><use href="#i-mic"/></svg></div>
  <div class="label" style="top:334px">Past intentions?</div>
  <div class="chip" style="left:16px;width:118px"><svg width="24" height="18" viewBox="0 0 24 24"><use href="#i-social"/></svg>Mediation</div>
  <div class="chip" style="left:146px;width:132px"><svg width="22" height="20" viewBox="0 0 24 24"><use href="#i-game"/></svg>Gym Hitting</div>
  <svg style="position:absolute;left:289px;top:381px" width="8" height="10" viewBox="0 0 8 10"><path d="M2 1l4 4-4 4" fill="none" stroke="#222" stroke-width="1.4"/></svg>
  <div class="label" style="top:431px">Set Timer</div>
  <div class="timer">07:00 <small>AM</small></div>
  <div class="timer__sub">Wake Up OR Others</div>
  <div class="toggle"></div>

  <nav class="nav">
    <div class="nav__item" style="left:35px"><svg><use href="#i-home"/></svg>Home</div>
    <div class="nav__item" style="left:87px"><svg><use href="#i-social"/></svg>Social<br>Features</div>
    <div class="nav__active" style="left:156px"><svg><use href="#i-target"/></svg></div>
    <span class="nav__active-label" style="left:156px">Daily Intentions</span>
    <div class="nav__item" style="left:225px"><svg><use href="#i-game"/></svg>Gamification</div>
    <div class="nav__item" style="left:276px"><svg><use href="#i-progress"/></svg>Progress<br>Tracking</div>
  </nav>
</section>

<!-- Social Features -->
<section class="phone phone--social">
  <div class="header"><div class="header__blob"></div><div class="header__pill"></div></div>
  <div class="status"><span>8:41 Am</span><svg width="58" height="12"><use href="#i-status"/></svg></div>
  <div class="title">Social Features</div>
  <div class="brand"><span class="brand__dot"></span><span class="brand__name">PathMentor</span></div>

  <div class="bubble bubble--in" style="top:143px">Lorem ipsum dolor s</div>
  <div class="bubble bubble--out" style="top:195px">Excepteur sint occaeca</div>
  <div class="bubble bubble--in" style="top:248px">Lorem ipsum dolor s</div>
  <div class="bubble bubble--out" style="top:300px">Excepteur sint occaeca</div>
  <div class="bubble bubble--in" style="top:352px">Lorem ipsum dolor s</div>
  <div class="bubble bubble--out" style="top:404px">Excepteur sint occaeca</div>

  <div class="composer">
    <svg width="17" height="17" viewBox="0 0 24 24"><g fill="none" stroke="#999" stroke-width="1.8"><circle cx="12" cy="12" r="10"/><path d="M7.5 14.5a5 5 0 0 0 9 0"/></g><circle cx="9" cy="10" r="1.3" fill="#999"/><circle cx="15" cy="10" r="1.3" fill="#999"/></svg>
    <span>Type a message</span>
    <span class="composer__tools">
      <svg width="15" height="15" viewBox="0 0 24 24"><path d="M20 11 12 19a5 5 0 0 1-7-7l8-8a3.3 3.3 0 0 1 4.7 4.7l-8 8a1.7 1.7 0 0 1-2.4-2.4L15 7" fill="none" stroke="#999" stroke-width="1.8"/></svg>
      <svg width="15" height="15" viewBox="0 0 24 24"><rect x="2" y="2" width="20" height="20" rx="4" fill="#999"/><circle cx="12" cy="13" r="4.5" fill="#fff"/><circle cx="12" cy="13" r="2.6" fill="#999"/></svg>
    </span>
  </div>
  <div class="mic-btn"><svg width="18" height="18" viewBox="0 0 24 24"><use href="#i-mic"/></svg></div>

  <nav class="nav">
    <div class="nav__item" style="left:35px"><svg><use href="#i-home"/></svg>Home</div>
    <div class="nav__active" style="left:87px"><svg><use href="#i-social"/></svg></div>
    <span class="nav__active-label" style="left:89px">Social Features</span>
    <div class="nav__item" style="left:161px;top:12px"><svg style="width:23px;height:23px"><use href="#i-target"/></svg>Daily<br>Intensions</div>
    <div class="nav__item" style="left:225px"><svg><use href="#i-game"/></svg>Gamification</div>
    <div class="nav__item" style="left:276px"><svg><use href="#i-progress"/></svg>Progress<br>Tracking</div>
  </nav>
</section>
</body>
</html>
```